Business card design needed

I need a business card design also to be used on fridge magnets. All the details above to be included on the card. I am a freelance book-keeper providing services to small to medium size business providing services in PLUV including training, consulting, BAS, IAS, preparation and lodgement, superannuation, workcover. I would like a design that is easy to read a see. Something that relates to the finance industry. A design that can be used for all other marketing products.

Target Market(s)

Small business mainly sole traders - trades people

Industry/Entity Type

Marketing

Contact Information for Business Card

Bramblewood Book-keeping Services Maren Vosk - PLUV Consultant BAS REGISTERED AGENT 27360519 PO Box 7316 Marlow Heights QLD 4187 0478152906

Logo Text

Bramblewood Book-keeping Services

Logo styles of interest
Emblem Logo
Pictorial/Combination Logo
Abstract Logo
Character Logo

```html
<!DOCTYPE html>
<html lang="en">
<head>
<meta charset="utf-8">
<title>Bramblewood Book-keeping Services – Business Card</title>
<link rel="stylesheet" href="https://fonts.googleapis.com/css2?family=Tenor+Sans&display=swap">
<style>
  :root {
    --backdrop: #2a2a2b;
    --card: #ffffff;
    --brand-green: #7dc242;
    --brand-blue: #3fb7e3;
    --ink: #4a4a4a;
    --label: #6b6b6b;
    --dot-grey: rgba(225, 225, 225, 0.85);
    --dot-blue: rgba(200, 230, 245, 0.9);
    --dot-green: rgba(220, 236, 198, 0.9);
    --clear: rgba(255, 255, 255, 0);
  }
  * { margin: 0; padding: 0; box-sizing: border-box; }
  html, body {
    width: 1200px;
    height: 900px;
    overflow: hidden;
    background: var(--backdrop);
    font-family: "Tenor Sans", "Optima", sans-serif;
  }
  .stage {
    width: 1200px;
    height: 900px;
    display: flex;
    align-items: center;
    justify-content: center;
  }
  .card {
    position: relative;
    width: 900px;
    height: 540px;
    background: var(--card);
    overflow: hidden;
  }
  .card__pattern {
    position: absolute;
    inset: 0;
    background:
      radial-gradient(circle 220px at 80% 22%, var(--dot-green) 0%, var(--clear) 100%),
      radial-gradient(circle 200px at 62% 38%, var(--dot-blue) 0%, var(--clear) 100%),
      radial-gradient(circle 200px at 88% 62%, var(--dot-green) 0%, var(--clear) 100%),
      radial-gradient(circle 200px at 52% 58%, var(--dot-grey) 0%, var(--clear) 100%);
  }
  .card__band {
    position: absolute;
    left: 0;
    right: 0;
    bottom: 0;
    height: 16px;
    background: var(--brand-green);
  }
  .brand {
    position: absolute;
    left: 60px;
    top: 110px;
    display: flex;
    align-items: center;
    gap: 18px;
  }
  .brand__dot {
    width: 46px;
    height: 46px;
    border-radius: 50%;
    background: var(--brand-blue);
  }
  .brand__name {
    color: var(--brand-green);
    font-size: 28px;
    line-height: 1.15;
    letter-spacing: 0.5px;
  }
  .person {
    position: absolute;
    left: 120px;
    top: 330px;
    color: var(--ink);
  }
  .person__name {
    color: var(--brand-blue);
    font-size: 34px;
    font-weight: 400;
    letter-spacing: 1px;
    margin-bottom: 8px;
  }
  .person__role {
    font-size: 18px;
    line-height: 1.45;
  }
  .contact {
    position: absolute;
    left: 500px;
    top: 250px;
    color: var(--ink);
  }
  .contact__phone {
    font-size: 30px;
    color: var(--brand-blue);
    margin-bottom: 10px;
  }
  .contact__label {
    font-size: 20px;
    color: var(--label);
  }
  .contact__address {
    font-size: 18px;
    line-height: 1.35;
  }
</style>
</head>
<body>
  <main class="stage">
    <article class="card">
      <div class="card__pattern" role="img" aria-label="Decorative field of soft grey, blue and green circles"></div>

      <div class="brand">
        <span class="brand__dot"></span>
        <div class="brand__name">Bramblewood<br>Book-keeping Services</div>
      </div>

      <section class="person">
        <h1 class="person__name">MAREN VOSK</h1>
        <p class="person__role">PLUV Consultant</p>
        <p class="person__role">BAS REGISTERED AGENT 27360519</p>
      </section>

      <section class="contact">
        <p class="contact__phone"><span class="contact__label">PH:</span> 0478152906</p>
        <p class="contact__address">PO Box 7316 Marlow Heights<br>QLD 4187</p>
      </section>

      <div class="card__band"></div>
    </article>
  </main>
</body>
</html>
```